Flier redesign

Sample fliers are attached from previous 2 years "Seasonal care 2018" and "2019 Seasonal Care" . Need an updated design for this year.

Possible images are attached to this brief. If you use the before/after pictures - you should use both of them. Use images attached to this brief or any from our website that you may prefer.

Colors

Designer to choose colors to be used in the design.

Requirements
Must have
• Colors should match our website theme. www.hollowbrookgardens.org
• Should be a "new" design, not just copying one of the prior year designs with a different image.
• Must be created in photoshop and file must be provided at the end.
• Text should be the same as 2019 version.

```html
<!DOCTYPE html>
<html lang="en">
<head>
<meta charset="utf-8">
<title>Hollowbrook Gardens – 2020 Landscaping Packages</title>
<link href="https://fonts.googleapis.com/css2?family=Saira+Condensed:wght@400;500;600;700;800&display=swap" rel="stylesheet">
<style>
  :root {
    --maroon: #7a1f2e;
    --charcoal: #3b3b3c;
    --mid-grey: #a6a7a8;
    --side-grey: #d3d4d5;
    --side-shade: #bfc0c1;
    --floor-grey: #6e6f6e;
    --body-text: #4b4b4c;
    --white: #ffffff;
  }
  * { box-sizing: border-box; margin: 0; padding: 0; }
  html, body { width: 928px; height: 1200px; overflow: hidden; }
  body { font-family: "Saira Condensed", "Arial Narrow", sans-serif; background: var(--floor-grey); }

  .flier { position: relative; width: 928px; height: 1200px; overflow: hidden; }

  .hero-photo {
    position: absolute; left: 0; top: 0; width: 928px; height: 849px;
    background:
      linear-gradient(180deg, rgba(0,0,0,0) 72%, rgba(80,120,50,0.9) 78%, #6f9a44 100%),
      radial-gradient(ellipse at 40% 35%, #b8361c 0%, #a52a18 35%, #c2521c 60%, #d97c26 80%, #e8d9c8 100%);
  }
  .maroon-band { position: absolute; left: 0; top: 849px; width: 928px; height: 293px; background: var(--maroon); }
  .floor-band { position: absolute; left: 0; top: 1142px; width: 928px; height: 58px; background: var(--floor-grey); }

  .brand-plate {
    position: absolute; left: 388px; top: 0; width: 151px; height: 172px;
    background: var(--white);
    display: flex; flex-direction: column; align-items: center; justify-content: flex-end;
    padding-bottom: 18px;
  }
  .brand-plate .brand-name {
    color: var(--maroon); font-weight: 600; font-size: 25px; line-height: 1.05;
    text-align: center; text-transform: uppercase; letter-spacing: 0.5px;
  }

  .title-block { position: absolute; left: 377px; top: 172px; width: 173px; text-align: center; color: var(--white); }
  .title-year { font-size: 52px; font-weight: 600; line-height: 58px; }
  .title-rule { height: 1px; background: var(--white); margin: 0 0 4px; }
  .title-name { font-size: 31px; font-weight: 500; line-height: 33px; text-transform: uppercase; }

  .package { position: absolute; bottom: 33px; }
  .package .side {
    position: absolute; left: 0; bottom: 0; width: 16px;
    background: linear-gradient(180deg, var(--side-shade) 0, var(--side-shade) var(--cap), var(--side-grey) var(--cap));
    clip-path: polygon(0 var(--slant), 100% 0, 100% 100%, 0 calc(100% - 8px));
  }
  .package .face { position: absolute; right: 0; bottom: 0; width: 147px; display: flex; flex-direction: column; }
  .package-name {
    background: var(--charcoal); color: var(--white); text-transform: uppercase;
    font-weight: 700; font-size: 22px; line-height: 20px; text-align: center; padding: 5px 2px 4px;
  }
  .package-tagline {
    background: var(--mid-grey); color: var(--white); font-size: 17px; line-height: 19px;
    text-align: center; display: flex; align-items: center; justify-content: center; padding: 0 4px;
  }
  .package-body { background: var(--white); flex: 1; display: flex; flex-direction: column; padding: 10px 6px 0 12px; color: var(--body-text); }
  .features { list-style: none; font-size: 16.5px; line-height: 17.5px; }
  .features li { position: relative; padding-left: 16px; margin-bottom: 14px; }
  .features li::before { content: "✓"; position: absolute; left: 0; top: 0; color: var(--maroon); font-weight: 700; }

  .pricing { color: var(--maroon); text-align: center; margin-top: auto; }
  .pricing .term { font-size: 21px; line-height: 24px; font-weight: 500; text-transform: uppercase; }
  .pricing .amount { font-size: 36px; line-height: 38px; font-weight: 800; }
  .price-tier + .price-tier { border-top: 1px solid var(--maroon); margin: 8px 18px 0; padding-top: 8px; }
  .price-tier { margin: 0 18px; }
  .fine-print { color: var(--maroon); font-size: 14px; line-height: 16px; text-align: center; margin: 18px 0 26px; }

  .popular-cap {
    position: absolute; right: 0; width: 147px; height: 40px;
    background: var(--charcoal); clip-path: polygon(0 100%, 50% 0, 100% 100%);
    color: var(--white); font-weight: 700; font-size: 12.5px; line-height: 13px; text-align: center;
    text-transform: uppercase; padding-top: 11px;
  }

  .package--perpetual { left: 103px; width: 163px; height: 760px; }
  .package--perpetual .side { height: 700px; --slant: 12px; --cap: 70px; }
  .package--perpetual .face { height: 720px; }
  .package--perpetual .popular-cap { top: 0; }
  .package--perpetual .package-tagline { height: 67px; }

  .package--seasonal { left: 383px; width: 162px; height: 601px; }
  .package--seasonal .side { height: 601px; --slant: 12px; --cap: 100px; }
  .package--seasonal .face { height: 601px; }
  .package--seasonal .package-tagline { height: 47px; }
  .package--seasonal .package-body { padding-top: 14px; }

  .package--basic { left: 661px; width: 162px; height: 549px; }
  .package--basic .side { height: 549px; --slant: 12px; --cap: 113px; }
  .package--basic .face { height: 549px; }
  .package--basic .package-tagline { height: 67px; }
  .package--basic .package-body { padding-top: 24px; }
</style>
</head>
<body>
<main class="flier">
  <div class="hero-photo" role="img" aria-label="Photograph of tall autumn maple trees with red and orange leaves over green cemetery lawns"></div>
  <div class="maroon-band"></div>
  <div class="floor-band"></div>

  <header class="brand-plate">
    <span class="brand-name">Hollowbrook<br>Gardens</span>
  </header>

  <div class="title-block">
    <div class="title-year">2020</div>
    <div class="title-rule"></div>
    <h1 class="title-name">Landscaping<br>Packages</h1>
  </div>

  <section class="package package--perpetual">
    <div class="side"></div>
    <div class="popular-cap">Most<br>Popular</div>
    <div class="face">
      <h2 class="package-name">Perpetual Care<br>Endowment</h2>
      <p class="package-tagline">Landscaping care forever for graves with no plantings</p>
      <div class="package-body">
        <ul class="features">
          <li>Weeding and trimming services on your gravesite approximately every 7 weeks during the growing season: mid-April through mid-October</li>
          <li>Monument leveling and cleaning</li>
          <li>Payment ensures grave care forever</li>
          <li>Full bed of boxwood shrubs</li>
          <li>Replacement of shrubs</li>
          <li>Trust certificate</li>
        </ul>
        <div class="pricing">
          <div class="term">12 Monthly<br>Payments of</div>
          <div class="amount">$297</div>
        </div>
        <p class="fine-print">Call for single payment discount.<br>Valid through 10/31/19.</p>
      </div>
    </div>
  </section>

  <section class="package package--seasonal">
    <div class="side"></div>
    <div class="face">
      <h2 class="package-name">Seasonal<br>Care</h2>
      <p class="package-tagline">Seasonal landscaping grave care</p>
      <div class="package-body">
        <ul class="features">
          <li>Weeding and trimming services on your gravesite approximately every 7 weeks during the growing season: mid-April through mid-October</li>
        </ul>
        <div class="pricing">
          <div class="price-tier"><div class="term">3 Years</div><div class="amount">$345</div></div>
          <div class="price-tier"><div class="term">2 Years</div><div class="amount">$230</div></div>
          <div class="price-tier"><div class="term">1 Years</div><div class="amount">$115</div></div>
        </div>
        <p class="fine-print">Multi-year payment locks in current rate.<br>Valid through 10/31/19</p>
      </div>
    </div>
  </section>

  <section class="package package--basic">
    <div class="side"></div>
    <div class="face">
      <h2 class="package-name">Basic Care<br>Endowment</h2>
      <p class="package-tagline">Landscaping care forever for graves with no plantings</p>
      <div class="package-body">
        <ul class="features">
          <li>Weeding and trimming services on your gravesite 2 times per year: mid-May and mid-September</li>
          <li>Monument leveling</li>
          <li>Payment ensures grave care forever</li>
        </ul>
        <div class="pricing">
          <div class="term">12 Monthly<br>Payments of</div>
          <div class="amount">$239</div>
        </div>
        <p class="fine-print">Call for single payment discount.<br>Valid through 10/31/19.</p>
      </div>
    </div>
  </section>
</main>
</body>
</html>
```